Funeral Services Site

We need a website for a Funeral Services company. The old website is: www.rouwcentrumkorvelaer.be We need the same structure and text.

Target Market(s)

Customers.

Coding

Coded - Design and coding required

Number of Pages Required

4 page

Font styles to use
Serif
Sans Serif
Script

```html
<!DOCTYPE html>
<html lang="en">
<head>
<meta charset="utf-8">
<title>Funeral Home Verhaegen Bvba</title>
<link href="https://fonts.googleapis.com/css2?family=Poppins:wght@300;400;500;600&display=swap" rel="stylesheet">
<style>
:root{
  --red:#e74c3c;
  --ink:#2b2b2b;
  --text:#3a3a3a;
  --muted:#555;
  --dark-a:#2f2f2f;
  --dark-b:#3a3a3a;
  --footer:#333333;
  --soft:#f2f2f2;
  --line:#d9d9d9;
  --white:#ffffff;
}
*{margin:0;padding:0;box-sizing:border-box}
html,body{width:1200px;height:3232px;overflow:hidden;background:var(--white)}
body{position:relative;font-family:'Poppins',sans-serif;color:var(--text)}
.abs{position:absolute}
.center{text-align:center}
svg.ico{display:inline-block;vertical-align:middle}

/* header */
.topline{left:0;top:0;width:1200px;height:3px;background:var(--red)}
.phone-tab{left:853px;top:0;width:225px;height:33px;background:var(--red);border-radius:0 0 14px 14px;color:var(--white);font-size:16px;display:flex;align-items:center;justify-content:center;gap:10px}
.brand-badge{left:143px;top:-44px;width:208px;height:208px;border-radius:50%;background:var(--white);box-shadow:0 4px 10px rgba(0,0,0,.25);display:flex;align-items:flex-end;justify-content:center;padding-bottom:34px}
.brand-name{font-size:15px;line-height:18px;color:var(--ink);text-align:center;font-weight:400}
.nav{top:56px;font-size:16px;color:var(--ink)}
.nav .active{color:var(--red);font-weight:500}

/* hero */
.hero{left:0;top:98px;width:1200px;height:437px;background:linear-gradient(100deg,#c9cf7a 0%,#6f8a4a 18%,#c77aa6 38%,#e8a6c4 50%,#3f7a4a 62%,#1fa05a 75%,#d9d2c6 88%,#e8e4de 100%)}
.hero-arrow{top:305px;width:26px;height:24px;background:#3a3a3a;display:flex;align-items:center;justify-content:center}
.hero-card{left:234px;top:498px;width:730px;height:189px;background:var(--white);border-top:3px solid var(--red);box-shadow:0 4px 12px rgba(0,0,0,.12)}
.hero-card h1{font-weight:400;font-size:29px;line-height:38px;color:var(--ink);text-align:center;margin-top:16px}
.pill{border:2px solid var(--red);border-radius:24px;background:var(--white);display:flex;align-items:center;justify-content:center;gap:14px;color:var(--ink);font-size:17px}
.pill .num{font-weight:500}

/* section heads */
.sec-title{font-weight:400;color:var(--ink);text-align:center;width:1200px;left:0}
.rule{height:2px;background:#444;width:84px;left:558px}
.btn{background:var(--red);color:var(--white);border-radius:16px;display:flex;align-items:center;justify-content:center}

/* about */
.about-sub{top:828px;left:0;width:1200px;text-align:center;font-size:18px;color:var(--ink)}
.about-copy{top:862px;left:150px;width:900px;text-align:center;font-size:13.5px;line-height:23.5px;color:var(--text)}

/* organization */
.photo-cross{left:143px;top:1151px;width:387px;height:375px;background:linear-gradient(180deg,#6a3a1e 0%,#8a5a34 40%,#e6e4d6 60%,#3e5a2e 80%,#3a4a8a 100%);box-shadow:0 6px 14px rgba(0,0,0,.2)}
.org-copy{left:553px;top:1188px;width:510px;font-size:13.5px;line-height:25px;color:var(--text)}
.org-copy p+p{margin-top:12px}
.arrange{left:553px;top:1364px;font-size:18px;color:var(--ink)}
.arrange-list{left:553px;top:1400px;font-size:14px;color:var(--text);list-style:none}
.arrange-list li{display:flex;gap:12px;align-items:flex-start;line-height:22px;margin-bottom:13px}

/* dark split */
.split-a{left:0;top:1614px;width:614px;height:479px;background:var(--dark-a)}
.split-b{left:614px;top:1614px;width:586px;height:479px;background:var(--dark-b)}
.split-title{font-size:32px;line-height:38px;color:var(--red);font-weight:300;text-align:center}
.split-rule{height:2px;width:34px;background:var(--white)}
.split-copy{font-size:13.5px;line-height:23px;color:#e6e6e6;text-align:center;font-weight:300}
.btn-get{font-size:16px;border-radius:16px}

/* quick contact */
.contact-band{left:0;top:2093px;width:1200px;height:538px;background:var(--soft)}
.contact-intro{left:165px;top:2234px;width:870px;text-align:center;font-size:14px;line-height:23px;color:var(--ink)}
.field{background:var(--white);border:1px solid var(--line);border-radius:3px;font-size:11.5px;font-weight:500;color:var(--ink);padding:6px 15px}

/* cta */
.cta-text{left:0;top:2710px;width:1200px;text-align:center;font-size:20px;line-height:36px;color:var(--ink);text-transform:uppercase}

/* footer */
.footer{left:0;top:2919px;width:1200px;height:266px;background:var(--footer)}
.foot-title{font-size:15px;color:var(--white)}
.foot-rule{height:2px;width:36px;background:var(--white)}
.foot-links{left:143px;top:3004px;list-style:none;font-size:13px;line-height:27.3px;color:var(--white)}
.foot-item{font-size:12.5px;line-height:18px;color:var(--white);display:flex;gap:12px;align-items:flex-start}
.foot-brand{left:784px;top:3030px;display:flex;align-items:center;gap:14px;color:var(--white);font-size:25px;line-height:30px;font-weight:500}
.foot-brand .mark{width:62px;height:62px;border-radius:50%;border:2px solid var(--white)}
.copybar{left:0;top:3185px;width:1200px;height:47px;background:var(--red);color:var(--white);font-size:13px;display:flex;align-items:center;justify-content:center}
</style>
</head>
<body>
<svg width="0" height="0" style="position:absolute">
  <defs>
    <symbol id="phone" viewBox="0 0 24 24">
      <circle cx="12" cy="12" r="10.5" fill="none" stroke="currentColor" stroke-width="1.6"/>
      <path d="M8.6 6.8c.4-.3 1-.2 1.2.2l1.1 2c.2.4.1.8-.2 1.1l-.7.6c.5 1.3 1.6 2.5 2.9 3.1l.6-.7c.3-.3.8-.4 1.1-.2l2 1.1c.4.2.5.8.2 1.2l-.8 1c-.5.6-1.3.8-2 .5-3-1.2-5.3-3.6-6.5-6.6-.3-.7 0-1.5.5-2z" fill="currentColor"/>
    </symbol>
    <symbol id="tick" viewBox="0 0 16 16">
      <circle cx="7.5" cy="8.5" r="6" fill="none" stroke="#e74c3c" stroke-width="1.3"/>
      <path d="M4.8 8.3l2.2 2.2L14 3.5" fill="none" stroke="#e74c3c" stroke-width="1.5"/>
    </symbol>
  </defs>
</svg>

<!-- header -->
<div class="abs topline"></div>
<div class="abs phone-tab"><svg class="ico" width="22" height="22" style="color:#fff"><use href="#phone"/></svg><span>1-555-010-2468</span></div>
<div class="abs brand-badge"><div class="brand-name">Funeral Home<br>Verhaegen Bvba</div></div>
<nav>
  <span class="abs nav active" style="left:500px">Home</span>
  <span class="abs nav" style="left:583px">About Us</span>
  <span class="abs nav" style="left:686px">Condole Online</span>
  <span class="abs nav" style="left:835px">Order Flowers</span>
  <span class="abs nav" style="left:972px">Contact Us</span>
</nav>

<!-- hero -->
<div class="abs hero" role="img" aria-label="Photo of a hand placing a flower arrangement with pink gerberas on a grave"></div>
<div class="abs hero-arrow" style="left:6px"><svg width="10" height="12"><path d="M7 1L2 6l5 5" fill="none" stroke="#fff" stroke-width="2"/></svg></div>
<div class="abs hero-arrow" style="left:1166px"><svg width="10" height="12"><path d="M3 1l5 5-5 5" fill="none" stroke="#fff" stroke-width="2"/></svg></div>
<div class="abs hero-card">
  <h1>Funeral Home Verhaegen Bvba:<br>A Personal Service In Farewell Guidance</h1>
</div>
<div class="abs pill" style="left:423px;top:606px;width:354px;height:45px">
  <span>Contact Us Today</span><svg class="ico" width="24" height="24" style="color:#2b3a55"><use href="#phone"/></svg><span class="num">1-555-010-2468</span>
</div>

<!-- about -->
<h2 class="abs sec-title" style="top:762px;font-size:33px">About Us</h2>
<div class="abs rule" style="top:808px"></div>
<p class="abs about-sub">Mourning center Verhaegen, a complete service in mourning and farewell guidance</p>
<p class="abs about-copy">Saying goodbye to a loved one is one of the toughest things in a lifetime. Funeral home Verhaegen in Heuvelrode takes care of all the practical and administrative matters involved. So you can say goodbye in peace.<br>Our people have a rich experience in farewell guidance and stand for 24 hours at 24 hours for you. Our fully renovated funeral home is open to you and your acquaintances, so that you can greet your loved one at any time of the day.</p>
<div class="abs btn" style="left:540px;top:966px;width:113px;height:30px;font-size:15px;font-weight:500">Read More</div>

<!-- organization -->
<h2 class="abs sec-title" style="top:1077px;font-size:35px">Organization Funeral And Worship</h2>
<div class="abs rule" style="top:1127px;left:536px;width:126px"></div>
<div class="abs photo-cross" role="img" aria-label="Photo of a brass cross above white orchids and calla lilies"></div>
<div class="abs org-copy">
  <p>The organization of the funeral ceremony is a moment of reflection, where the personality of the deceased can be beautifully highlighted. Our team will assist you in this and select the most beautiful texts, songs and photos with you in order to arrive at an appropriate and worthy goodbye.</p>
  <p>The funeral can take place in your parish church or &nbsp;our auditorium if you wish, which can accommodate a maximum of 100 guests.</p>
</div>
<div class="abs arrange">We can arrange the following for you:</div>
<ul class="abs arrange-list">
  <li><svg class="ico" width="16" height="16" style="margin-top:3px"><use href="#tick"/></svg><span>Vigil The Night Before The Funeral</span></li>
  <li><svg class="ico" width="16" height="16" style="margin-top:3px"><use href="#tick"/></svg><span>Prayer Service With Priest (if Possible)</span></li>
  <li><svg class="ico" width="16" height="16" style="margin-top:3px"><use href="#tick"/></svg><span>Eucharistic Celebration With Priest<br>(on Tuesday And Friday In The Parishes Of Heuvelrode)</span></li>
</ul>

<!-- split -->
<div class="abs split-a"></div>
<div class="abs split-b"></div>
<h3 class="abs split-title" style="left:120px;top:1742px;width:400px">Condole Online via<br>the website</h3>
<div class="abs split-rule" style="left:303px;top:1826px"></div>
<p class="abs split-copy" style="left:130px;top:1840px;width:380px">Do you want to leave nice words to the family of a deceased person?<br>Funeral home Verhaegen gives you the opportunity to convey your message quickly and discreetly</p>
<div class="abs btn btn-get" style="left:256px;top:1946px;width:113px;height:30px">Get Started</div>

<svg class="abs" style="left:521px;top:1789px" width="160" height="160" viewBox="0 0 160 160">
  <circle cx="80" cy="80" r="79" fill="none" stroke="#555" stroke-width="1"/>
  <circle cx="80" cy="80" r="64" fill="none" stroke="#6a6a6a" stroke-width="1"/>
  <circle cx="80" cy="80" r="48" fill="#2f2f2f" stroke="#fff" stroke-width="2"/>
</svg>

<h3 class="abs split-title" style="left:678px;top:1738px;width:400px">Reserve Flower<br>Arrangement</h3>
<div class="abs split-rule" style="left:861px;top:1826px"></div>
<p class="abs split-copy" style="left:700px;top:1840px;width:360px">In the funeral home there is always an engaging selection of floral arrangements and wreaths .<br>If you want to order fresh flowers, consult the catalog in the store or complete the order form</p>
<div class="abs btn btn-get" style="left:819px;top:1951px;width:113px;height:30px">Get Started</div>

<!-- quick contact -->
<div class="abs contact-band"></div>
<h2 class="abs sec-title" style="top:2173px;font-size:33px">Quick Contact</h2>
<div class="abs rule" style="top:2222px"></div>
<p class="abs contact-intro">Lorem ipsum dolor sit amet, consectetuer adipiscing elit, sed diam nonummy nibh euismod tincidunt ut laoreet dolore magna aliquam erat volutpat. Ut wisi enim ad minim veniam.</p>
<div class="abs field" style="left:301px;top:2292px;width:290px;height:37px">First Name</div>
<div class="abs field" style="left:608px;top:2292px;width:289px;height:37px;padding-top:18px">Last Name</div>
<div class="abs field" style="left:301px;top:2344px;width:290px;height:37px">Email</div>
<div class="abs field" style="left:608px;top:2344px;width:289px;height:37px;padding-top:18px">Phone</div>
<div class="abs field" style="left:301px;top:2401px;width:596px;height:86px;padding-top:10px">Message</div>
<div class="abs btn" style="left:543px;top:2508px;width:105px;height:30px;font-size:12px;font-weight:600">SUBMIT</div>

<!-- cta -->
<p class="abs cta-text">Do you have any questions or would you like to call in our funeral home?<br>Contact us. We are here for you.</p>
<div class="abs pill" style="left:416px;top:2795px;width:354px;height:44px">
  <span>Contact Us Today</span><svg class="ico" width="24" height="24" style="color:#2b3a55"><use href="#phone"/></svg><span class="num">1-555-010-2468</span>
</div>

<!-- footer -->
<footer>
<div class="abs footer"></div>
<div class="abs foot-title" style="left:143px;top:2956px">Quick Links</div>
<div class="abs foot-rule" style="left:143px;top:2987px"></div>
<ul class="abs foot-links">
  <li>Home</li><li>About Us</li><li>Condole Online</li><li>Order Flowers</li><li>Contact Us</li>
</ul>
<div class="abs foot-title" style="left:374px;top:2959px">Contact Details</div>
<div class="abs foot-rule" style="left:374px;top:2989px"></div>
<div class="abs foot-item" style="left:374px;top:3010px">
  <svg width="14" height="20" viewBox="0 0 14 20" style="margin-top:2px"><path d="M7 1a6 6 0 0 0-6 6c0 4.5 6 12 6 12s6-7.5 6-12a6 6 0 0 0-6-6z" fill="#fff"/><circle cx="7" cy="7" r="2.3" fill="#333"/></svg>
  <span>Funeral Home Verhaegen Bvba:<br>Lindeweg 14, 3790 Heuvelrode</span>
</div>
<div class="abs foot-item" style="left:374px;top:3073px;align-items:center">
  <svg class="ico" width="18" height="18" style="color:#fff"><use href="#phone"/></svg>
  <span>24/24, 7 out of 7 &nbsp;- 012 00 11 22</span>
</div>
<div class="abs foot-item" style="left:374px;top:3116px;align-items:center">
  <svg width="18" height="13" viewBox="0 0 18 13"><rect x="1" y="1" width="16" height="11" fill="none" stroke="#fff" stroke-width="1.4"/><path d="M1 1l8 6 8-6" fill="none" stroke="#fff" stroke-width="1.4"/></svg>
  <span>mourningcenter.verhaegen@mailbox.example</span>
</div>
<div class="abs foot-brand"><span>Funeral home<br>Verhaegen bvba</span><span class="mark"></span></div>
<div class="abs copybar">Copyright © 2019 &nbsp;2018 Nordlight Media &nbsp;- Sitemap &nbsp;- Privacy Policy</div>
</footer>
</body>
</html>
```